Single Page Timetracking Dashboard Desktop App UI Design (Figma Link required)

Main Idea: a SaaS tool where employees can add their time and project in a playful way. There is a infographics and a list with tasks as well.

Based on the attached concept.png the brief is following:

- check the attached rough scribble
- add own ideas or change things if they add value
- Style: colourful, nerdy, professional saas, modern, beautiful, white space
- Quality expectation: inspiration1+2.png
- I will need a Figma link
- desktop only
- make something fresh and unique

Process:
I need to include 2-3 feedback rounds that will span probably around 7 days

Target Market(s)

Internal Business Tool for a Software Development Company

Industry/Entity Type

IT

Other font styles liked:
• Could be monospace, not a must though

Requirements
Must have
• At least one page; Figma Link to the design;
Nice to have
• Microinterations like drop-down, hover/active colors; functionality specifications
Should not have
• Mobile view

```html
<!DOCTYPE html>
<html lang="en">
<head>
<meta charset="utf-8">
<title>Track Your Time – Dashboard</title>
<link href="https://fonts.googleapis.com/css2?family=Nunito+Sans:wght@400;600;700;800&display=swap" rel="stylesheet">
<style>
:root{
  --bg:#f5f3f4; --card:#ffffff; --ink:#1d1d26; --muted:#4a4a55; --line:#d9d6da;
  --purple:#9b3bff; --purple-soft:#f3e8ff;
  --blue:#2ea8f7; --blue-soft:#e6f3fd;
  --green:#8ac926; --green-soft:#f1f6e7;
  --orange:#fb9a3c; --red:#f8574a; --slate:#4a4a6a;
  --coral-a:#fbb196; --coral-b:#f8837a;
  --sky-a:#5fb8f6; --sky-b:#3a92ea;
  --teal-a:#82d9ca; --teal-b:#16cfaf;
}
*{box-sizing:border-box;margin:0;padding:0}
html,body{width:1200px;height:2470px;overflow:hidden}
body{background:var(--bg);font-family:"Nunito Sans",sans-serif;color:var(--ink);position:relative}
.abs{position:absolute}
.sidebar{left:0;top:0;width:91px;height:2470px;background:var(--card);border-radius:0 24px 24px 0}
.nav-active{left:20px;top:31px;width:50px;height:52px;border-radius:12px;background:var(--purple);display:flex;align-items:center;justify-content:center;box-shadow:0 4px 10px rgba(155,59,255,.35)}
.nav-icon{left:30px;width:30px;height:30px}
.logout-btn{left:20px;top:2374px;width:48px;height:48px;border-radius:50%;background:linear-gradient(135deg,#ff6a5a,#e9362f);display:flex;align-items:center;justify-content:center}
.logout-label{left:22px;top:2438px;font-size:13px;color:var(--muted)}
.h1{font-weight:800;font-size:20px;letter-spacing:.2px}
.card{background:var(--card);border-radius:8px}
.cal{left:163px;top:89px;width:264px;height:240px}
.cal-title{left:20px;top:16px;font-size:12px;font-weight:600}
.cal-arrows{right:20px;top:18px;font-size:9px;letter-spacing:12px}
.cal-grid{left:12px;top:50px;display:grid;grid-template-columns:repeat(7,34.8px);grid-auto-rows:33.5px;font-size:9.5px;text-align:center;color:var(--muted)}
.cal-grid .dow{font-size:8.5px;line-height:14px;height:22px}
.cal-grid span{line-height:22px}
.cal-grid .today{width:24px;height:24px;border-radius:50%;margin:0 auto;background:var(--coral-b);color:#fff;line-height:24px}
.select{left:443px;width:264px;height:42px;display:flex;align-items:center;justify-content:space-between;padding:0 8px 0 17px;font-size:12.5px}
.caret{width:22px;height:22px;border-radius:5px;background:linear-gradient(135deg,var(--coral-a),var(--coral-b));display:flex;align-items:center;justify-content:center}
.link{left:443px;font-size:11px;text-decoration:underline;color:var(--ink)}
.chip{width:100px;height:61px;border-radius:6px;display:flex;align-items:center;justify-content:center;font-size:17px;color:#fff}
.chip.sky{background:linear-gradient(135deg,var(--sky-a),var(--sky-b))}
.chip.coral{background:linear-gradient(135deg,var(--coral-a),var(--coral-b));color:var(--ink)}
.chip.plain{background:var(--card);color:var(--ink);font-size:16px}
.and{left:940px;top:238px;font-size:14px}
.notes{left:163px;top:353px;width:539px;height:109px;padding:21px;font-size:14px}
.tbox{top:353px;width:75px;height:109px;border-radius:6px;background:var(--purple);color:#fff;text-align:center;padding-top:20px;box-shadow:0 3px 8px rgba(155,59,255,.3)}
.tbox b{display:block;font-weight:400;font-size:31px;line-height:34px}
.tbox i{font-style:normal;font-size:18px}
.colon{left:829px;top:388px;color:var(--purple);font-size:20px;line-height:12px;width:8px;text-align:center}
.save{left:990px;top:353px;width:189px;height:109px;border-radius:6px;background:linear-gradient(135deg,var(--teal-a),var(--teal-b));color:#fff;font-size:25px;font-weight:700;display:flex;align-items:center;justify-content:center}
.month-select{left:1051px;top:526px;width:128px;height:43px}
.stat{top:589px;height:333px}
.stat-head{left:29px;right:23px;top:22px;display:flex;justify-content:space-between;font-size:17px;font-weight:600;padding-bottom:12px;border-bottom:1px solid var(--line)}
.pill{border-radius:6px;font-size:11.5px;padding:0 12px;display:flex;align-items:center;color:var(--ink)}
.legend{position:absolute;width:173px;height:26px;font-size:10.5px;justify-content:center}
.btn-coral{background:linear-gradient(135deg,var(--coral-a),var(--coral-b));border-radius:9px;font-size:14px;width:80px;height:32px;display:flex;align-items:center;justify-content:center;color:var(--ink)}
.filter{left:1096px;top:1042px;width:79px;height:31px;border-radius:6px;background:var(--green);color:#fff;font-size:13.5px;display:flex;align-items:center;justify-content:center;gap:6px}
.day{left:164px;font-size:18px;font-weight:800}
.day-total{right:30px;font-size:18px;font-weight:700}
.task{left:163px;width:1012px;height:168px}
.task-bar{position:absolute;left:8px;right:8px;top:8px;height:37px;border-radius:6px;display:flex;align-items:center;padding:0 10px 0 15px;font-size:12.5px;gap:6px}
.task-bar .actions{margin-left:auto;display:flex;gap:8px}
.dot{width:23px;height:23px;border-radius:50%;display:flex;align-items:center;justify-content:center}
.task h3{position:absolute;left:34px;top:64px;font-weight:400;font-size:20.5px}
.task p{position:absolute;left:35px;top:100px;width:620px;font-size:12.5px;line-height:20px;color:var(--muted)}
.task .dur{position:absolute;right:21px;top:66px;font-size:27px}
.task .date{position:absolute;right:21px;top:115px;width:111px;height:31px;border-radius:8px;border:1px solid;display:flex;align-items:center;justify-content:center;font-size:14px;color:var(--ink)}
.t-blue .task-bar{background:var(--blue-soft)} .t-blue .dot{background:var(--blue)} .t-blue .dur{color:var(--blue)} .t-blue .date{border-color:var(--blue)}
.t-green .task-bar{background:var(--green-soft)} .t-green .dot{background:var(--green)} .t-green .dur{color:var(--green)} .t-green .date{border-color:var(--green)}
.t-purple .task-bar{background:var(--purple-soft)} .t-purple .dot{background:var(--purple)} .t-purple .dur{color:var(--purple)} .t-purple .date{border-color:var(--purple)}
</style>
</head>
<body>

<svg width="0" height="0" style="position:absolute">
  <defs>
    <symbol id="i-trash" viewBox="0 0 24 24"><path d="M7 8h10l-1 12H8z M5 6h14 M10 4h4" fill="none" stroke="#fff" stroke-width="2"/></symbol>
    <symbol id="i-edit" viewBox="0 0 24 24"><path d="M5 5h8 M5 5v14h14v-8 M10 14l1-4 8-8 3 3-8 8z" fill="none" stroke="#fff" stroke-width="2"/></symbol>
    <symbol id="i-code" viewBox="0 0 24 24"><path d="M8 7l-5 5 5 5 M16 7l5 5-5 5 M14 5l-4 14" fill="none" stroke="#333" stroke-width="2"/></symbol>
    <symbol id="i-clock" viewBox="0 0 24 24"><circle cx="12" cy="12" r="9" fill="none" stroke="#333" stroke-width="2"/><path d="M12 7v5l3 2" fill="none" stroke="#333" stroke-width="2"/></symbol>
    <symbol id="i-meet" viewBox="0 0 24 24"><circle cx="9" cy="14" r="4" fill="none" stroke="#333" stroke-width="1.8"/><circle cx="16" cy="7" r="4" fill="none" stroke="#333" stroke-width="1.8"/><path d="M3 22c0-3 3-4 6-4 M12 12c2-1 6-1 8 1" fill="none" stroke="#333" stroke-width="1.8"/></symbol>
    <symbol id="i-down" viewBox="0 0 24 24"><path d="M6 9l6 6 6-6" fill="none" stroke="#fff" stroke-width="2.5"/></symbol>
  </defs>
</svg>

<aside class="sidebar abs">
  <div class="nav-active abs"><svg width="28" height="28"><use href="#i-clock" style="--c:#fff"/><circle cx="14" cy="14" r="10" fill="none" stroke="#fff" stroke-width="2"/><path d="M14 8v6l4 2" fill="none" stroke="#fff" stroke-width="2"/></svg></div>
  <svg class="nav-icon abs" style="top:120px" viewBox="0 0 30 30"><path d="M4 26h23 M6 24v-6 M11 24v-9 M16 24v-7 M21 24v-11 M25 24v-13 M5 16l6-6 5 4 9-10" fill="none" stroke="#333" stroke-width="1.5"/></svg>
  <svg class="nav-icon abs" style="top:188px" viewBox="0 0 30 30"><rect x="5" y="5" width="20" height="23" rx="2" fill="none" stroke="#333" stroke-width="1.5"/><path d="M9 3v4 M13 3v4 M17 3v4 M21 3v4 M9 12h12 M9 16h12 M9 20h12 M9 24h8" stroke="#333" stroke-width="1.5"/></svg>
  <svg class="nav-icon abs" style="top:258px" viewBox="0 0 30 30"><circle cx="15" cy="10" r="6" fill="none" stroke="#333" stroke-width="1.6"/><path d="M4 28c0-7 5-10 11-10s11 3 11 10z" fill="none" stroke="#333" stroke-width="1.6"/></svg>
  <div class="logout-btn abs"><svg width="26" height="26" viewBox="0 0 24 24"><path d="M8 3h10v18H8 M8 3v6 M8 15v6 M3 12h10 M10 9l3 3-3 3" fill="none" stroke="#fff" stroke-width="2"/></svg></div>
  <div class="logout-label abs">Logout</div>
</aside>

<h1 class="h1 abs" style="left:159px;top:45px">TRACK YOUR TIME</h1>

<section class="card cal abs">
  <div class="cal-title abs">October 2023</div>
  <div class="cal-arrows abs">▲▼</div>
  <div class="cal-grid abs">
    <span class="dow">Su</span><span class="dow">Mo</span><span class="dow">Tu</span><span class="dow">We</span><span class="dow">Th</span><span class="dow">Fr</span><span class="dow">Sa</span>
    <span>1</span><span>2</span><span>3</span><span>4</span><span>5</span><span>6</span><span>7</span>
    <span>8</span><span>9</span><span>10</span><span>11</span><span>12</span><span>13</span><span>14</span>
    <span>15</span><span>16</span><span>17</span><span>18</span><span>19</span><span>20</span><span>21</span>
    <span>22</span><span>23</span><span>24</span><span>25</span><span>26</span><span>27</span><span><span class="today">28</span></span>
    <span>29</span><span>30</span><span>31</span>
  </div>
</section>

<div class="card select abs" style="top:89px">Select Project<span class="caret"><svg width="14" height="14"><use href="#i-down"/></svg></span></div>
<div class="card select abs" style="top:142px">Select Type<span class="caret"><svg width="14" height="14"><use href="#i-down"/></svg></span></div>
<a class="link abs" style="top:205px">Customer 1 Project 1</a>
<a class="link abs" style="top:237px">Customer 2 Project 2</a>
<a class="link abs" style="top:271px">Customer 1 Project 2</a>
<a class="link abs" style="top:304px">Customer with long name andd projey</a>

<div class="chip coral abs" style="left:739px;top:89px">1h</div>
<div class="chip sky abs" style="left:852px;top:89px">2h</div>
<div class="chip sky abs" style="left:965px;top:89px">3h</div>
<div class="chip sky abs" style="left:1077px;top:89px">4h</div>
<div class="chip sky abs" style="left:739px;top:161px">5h</div>
<div class="chip sky abs" style="left:852px;top:161px">6h</div>
<div class="chip sky abs" style="left:965px;top:161px">7h</div>
<div class="chip sky abs" style="left:1077px;top:161px">8h</div>
<div class="and abs">AND</div>
<div class="chip plain abs" style="left:739px;top:268px">0m</div>
<div class="chip coral abs" style="left:852px;top:268px">15m</div>
<div class="chip plain abs" style="left:965px;top:268px">30m</div>
<div class="chip plain abs" style="left:1077px;top:268px">45m</div>

<div class="card notes abs">What did you do?</div>
<div class="tbox abs" style="left:744px"><b>1</b><i>h</i></div>
<div class="colon abs">·<br><br>·</div>
<div class="tbox abs" style="left:848px"><b>15</b><i>m</i></div>
<div class="save abs">SAVE</div>

<h2 class="h1 abs" style="left:163px;top:536px">STATISTICS</h2>
<div class="card select month-select abs" style="left:1051px;padding-left:14px">Monate<span class="caret"><svg width="14" height="14"><use href="#i-down"/></svg></span></div>

<section class="card stat abs" style="left:163px;width:493px">
  <div class="stat-head abs"><span>Current Month</span><span>Total : 50:45h</span></div>
  <svg class="abs" style="left:37px;top:91px" width="208" height="208" viewBox="-104 -104 208 208" role="img" aria-label="Pie chart: Customer A 89%, Customer B 11%">
    <g transform="scale(1.04)">
      <path d="M0 0 L-86.2 50.6 A100 100 0 1 1 -34.2 94 Z" fill="var(--purple)"/>
      <path d="M0 0 L-34.2 94 A100 100 0 0 1 -86.2 50.6 Z" fill="var(--green)"/>
    </g>
    <text x="-26" y="-44" fill="#fff" font-size="16" text-anchor="middle">A 89%</text>
    <text x="-36" y="50" fill="#fff" font-size="12" text-anchor="middle" transform="rotate(-55 -36 50)">B 11%</text>
  </svg>
  <div class="pill abs" style="left:285px;top:153px;height:26px;background:var(--purple-soft)">40:45 h Customer A (89% )</div>
  <div class="pill abs" style="left:285px;top:189px;height:26px;background:var(--green-soft)">08:15 h Customer B (11%))</div>
</section>

<section class="card stat abs" style="left:684px;width:494px">
  <div class="stat-head abs"><span>September</span><span>Gesamt : 114:00 h</span></div>
  <svg class="abs" style="left:34px;top:97px" width="212" height="212" viewBox="-106 -106 212 212" role="img" aria-label="Pie chart: Customers A to F">
    <g transform="scale(1.05)">
      <path d="M0 0 L-100 0 A100 100 0 0 1 0 -100 Z" fill="var(--blue)"/>
      <path d="M0 0 L0 -100 A100 100 0 0 1 81.9 -57.4 Z" fill="var(--purple)"/>
      <path d="M0 0 L81.9 -57.4 A100 100 0 0 1 94 34.2 Z" fill="var(--red)"/>
      <path d="M0 0 L94 34.2 A100 100 0 0 1 -34.2 94 Z" fill="var(--orange)"/>
      <path d="M0 0 L-34.2 94 A100 100 0 0 1 -86.6 50 Z" fill="var(--green)"/>
      <path d="M0 0 L-86.6 50 A100 100 0 0 1 -100 0 Z" fill="var(--slate)"/>
    </g>
    <g fill="#fff" text-anchor="middle">
      <text x="-40" y="-52" font-size="13">A</text><text x="-40" y="-34" font-size="13">53%</text>
      <text x="30" y="-54" font-size="10" transform="rotate(-62 30 -54)">F 34%</text>
      <text x="68" y="-4" font-size="10">E 13%</text>
      <text x="16" y="44" font-size="13">D</text><text x="16" y="64" font-size="13">53%</text>
      <text x="-42" y="56" font-size="10" transform="rotate(-52 -42 56)">C 34%</text>
      <text x="-64" y="22" font-size="10" transform="rotate(-14 -64 22)">B 13%</text>
    </g>
  </svg>
  <div class="pill legend abs" style="left:299px;top:97px;background:var(--blue-soft)">40:45 h Customer A (53% )</div>
  <div class="pill legend abs" style="left:299px;top:133px;background:#e9e9ee">08:15 h Customer B (13%)</div>
  <div class="pill legend abs" style="left:299px;top:169px;background:var(--green-soft)">20:00 H Customer C (34%)</div>
  <div class="pill legend abs" style="left:299px;top:205px;background:#fdf0e4">22:45 Hh Customer D (53%)</div>
  <div class="pill legend abs" style="left:299px;top:241px;background:#fde9e6">02:15 h Customer E (13%)</div>
  <div class="pill legend abs" style="left:299px;top:277px;background:var(--purple-soft)">20:00 h Customer F (34%)</div>
</section>

<div class="btn-coral abs" style="left:624px;top:954px">Show All</div>

<h2 class="h1 abs" style="left:163px;top:1045px">YOUR TASKS</h2>
<div class="filter abs"><svg width="16" height="16" viewBox="0 0 24 24"><path d="M5 3v18 M12 3v18 M19 3v18" stroke="#fff" stroke-width="2"/><path d="M2 8h6 M9 15h6 M16 10h6" stroke="#fff" stroke-width="3"/></svg>Filter</div>

<h3 class="day abs" style="top:1101px">WEDNESDAY</h3>
<div class="day-total abs" style="top:1101px">7H 30M</div>

<article class="card task t-blue abs" style="top:1141px">
  <div class="task-bar"><svg width="14" height="14"><use href="#i-code"/></svg>Coding<span class="actions"><span class="dot"><svg width="13" height="13"><use href="#i-trash"/></svg></span><span class="dot"><svg width="13" height="13"><use href="#i-edit"/></svg></span></span></div>
  <h3>Customer A Project 1</h3>
  <p>Sed ut perspiciatis unde omnis iste natus error sit voluptatem accusantium doloremque laudantium, totam rem aperiam, eaque ipsa quae ab illo inventore veritatis et quasi architecto</p>
  <div class="dur">4h 30m</div><div class="date">December 9th</div>
</article>

<h3 class="day abs" style="top:1343px">TUESDAY</h3>
<div class="day-total abs" style="top:1343px">7H 30M</div>

<article class="card task t-green abs" style="top:1386px">
  <div class="task-bar"><svg width="14" height="14"><use href="#i-clock"/></svg>Project Management<span class="actions"><span class="dot"><svg width="13" height="13"><use href="#i-trash"/></svg></span><span class="dot"><svg width="13" height="13"><use href="#i-edit"/></svg></span></span></div>
  <h3>Customer B Project 1</h3>
  <p>Sed ut perspiciatis unde omnis iste natus error sit voluptatem accusantium doloremque laudantium, totam rem aperiam, eaque ipsa quae ab illo inventore veritatis et quasi architecto</p>
  <div class="dur">3h</div><div class="date">December 9th</div>
</article>

<article class="card task t-green abs" style="top:1575px">
  <div class="task-bar"><svg width="14" height="14"><use href="#i-clock"/></svg>Project Management<span class="actions"><span class="dot"><svg width="13" height="13"><use href="#i-trash"/></svg></span><span class="dot"><svg width="13" height="13"><use href="#i-edit"/></svg></span></span></div>
  <h3>Customer B Project 1</h3>
  <p>Sed ut perspiciatis unde omnis iste natus error sit voluptatem accusantium doloremque laudantium, totam rem aperiam, eaque ipsa quae ab illo inventore veritatis et quasi architecto</p>
  <div class="dur">3h</div><div class="date">December 9th</div>
</article>

<article class="card task t-blue abs" style="top:1766px">
  <div class="task-bar"><svg width="14" height="14"><use href="#i-code"/></svg>Coding<span class="actions"><span class="dot"><svg width="13" height="13"><use href="#i-trash"/></svg></span><span class="dot"><svg width="13" height="13"><use href="#i-edit"/></svg></span></span></div>
  <h3>Customer A Project 1</h3>
  <p>Sed ut perspiciatis unde omnis iste natus error sit voluptatem accusantium doloremque laudantium, totam rem aperiam, eaque ipsa quae ab illo inventore veritatis et quasi architecto</p>
  <div class="dur">4h 30m</div><div class="date">December 9th</div>
</article>

<h3 class="day abs" style="top:1966px">MONDAY</h3>

<article class="card task t-purple abs" style="top:2006px">
  <div class="task-bar"><svg width="16" height="16"><use href="#i-meet"/></svg>Meeting<span class="actions"><span class="dot"><svg width="13" height="13"><use href="#i-trash"/></svg></span><span class="dot"><svg width="13" height="13"><use href="#i-edit"/></svg></span></span></div>
  <h3>Customer A Project 1</h3>
  <p>Sed ut perspiciatis unde omnis iste natus error sit voluptatem accusantium doloremque laudantium, totam rem aperiam, eaque ipsa quae ab illo inventore veritatis et quasi architecto</p>
  <div class="dur">4h 30m</div><div class="date">December 9th</div>
</article>

<article class="card task t-purple abs" style="top:2194px">
  <div class="task-bar"><svg width="16" height="16"><use href="#i-meet"/></svg>Meeting<span class="actions"><span class="dot"><svg width="13" height="13"><use href="#i-trash"/></svg></span><span class="dot"><svg width="13" height="13"><use href="#i-edit"/></svg></span></span></div>
  <h3>Customer A Project 1</h3>
  <p>Sed ut perspiciatis unde omnis iste natus error sit voluptatem accusantium doloremque laudantium, totam rem aperiam, eaque ipsa quae ab illo inventore veritatis et quasi architecto</p>
  <div class="dur">4h 30m</div><div class="date">December 9th</div>
</article>

<div class="btn-coral abs" style="left:624px;top:2390px">Show All</div>

</body>
</html>
```